Velmira Body Oil Label for 4 -8 oz bottles

We are selling 4 and 8 oz body oils and need a label to put on our bottles. I'm not sure if we want a label for the front and also the back of the bottle or just one label in the front. You can give me examples of each way. Attached is our logo on a blue background but the background will change colors depending on the scent as specified in the design description. Our bottle will be either clear or white with a pump spray type lid as shown in the attached example. Attached are also our design criteria which is needed for the labels.
Updates

We have decided to use the disc top cap and not the pump spray cap. If you are able to, please show us the design on the 4 oz bottle with the disc top cap. Thanks

Target Market(s)

women

Industry/Entity Type

skincare, cosmetics

Font styles to use
Serif
Sans Serif

Requirements
Must have
• stylish name for each scented oil which contrasts the font in the logo. Also must have darker colors since the logo colors are lighter.
Nice to have
• Border around the labels, maybe one solid color or maybe two complimenting colors which go well with the fragrnace name
Should not have
• background colors that match the logo colors

```html
<!DOCTYPE html>
<html lang="en">
<head>
<meta charset="utf-8">
<title>Velmira Body Oil Labels</title>
<link rel="stylesheet" href="https://fonts.googleapis.com/css2?family=Bodoni+Moda:wght@400;500&family=Montserrat:wght@400&display=swap">
<style>
  :root {
    --page: #ffffff;
    --label: #f5f5f5;
    --label-edge: #e2e2e2;
    --ink: #2e2e2e;
    --rule-dark: #3a3a3a;
    --cotton-name: #de9cbd;
    --cotton-panel-a: #5fd0ea;
    --cotton-panel-b: #1f95bb;
    --cotton-rule: #e8a9c6;
    --cotton-drop: #2aaed3;
    --lavender-name: #8d4f99;
    --lavender-panel-a: #bb8cc3;
    --lavender-panel-b: #6e2f7a;
    --lavender-drop: #8f4d9c;
    --vine-name: #3d5e3a;
    --vine-panel-a: #7c9a77;
    --vine-panel-b: #0e3410;
    --vine-drop: #2f5a2c;
    --fruity-name: #e3a62f;
    --fruity-panel-a: #f6cd6a;
    --fruity-panel-b: #cf8412;
    --fruity-drop: #e3a52d;
    --panel-text-light: #f1f1f1;
  }
  * { box-sizing: border-box; margin: 0; padding: 0; }
  html, body { width: 1200px; height: 1200px; overflow: hidden; background: var(--page); }
  .label-set {
    position: absolute; left: 60px; top: 240px;
    display: flex; gap: 40px;
  }
  .label {
    width: 240px; height: 720px;
    background: linear-gradient(90deg, #ebebeb, var(--label) 30%, #fafafa 60%, #e6e6e6);
    border: 1px solid var(--label-edge);
    border-radius: 16px;
    position: relative; overflow: hidden;
    font-family: "Bodoni Moda", serif;
  }
  .brand {
    position: absolute; top: 170px; left: 0; right: 0;
    display: flex; align-items: center; justify-content: center; gap: 8px;
  }
  .brand-dot { width: 12px; height: 12px; border-radius: 50%; }
  .brand-name {
    font-size: 34px; font-weight: 400; color: var(--ink); letter-spacing: 1px;
  }
  .scent-name {
    position: absolute; top: 300px; left: 0; right: 0; height: 120px;
    display: flex; flex-direction: column; align-items: center; justify-content: center;
    font-size: 56px; line-height: 0.98; font-weight: 400; text-transform: uppercase;
  }
  .scent-name span { display: inline-block; transform: scaleX(0.62); white-space: nowrap; }
  .band-rule {
    position: absolute; top: 457px; left: 0; right: 0; height: 7px; background: var(--rule-dark);
  }
  .type-box {
    position: absolute; top: 438px; left: 58px; width: 124px; height: 42px;
    background: #fff; border: 1px solid #555;
    display: flex; align-items: center; justify-content: center;
    font-size: 32px; color: var(--ink);
  }
  .type-box span { display: inline-block; transform: scaleX(0.62); white-space: nowrap; }
  .panel {
    position: absolute; top: 464px; left: 0; right: 0; height: 176px;
    color: var(--panel-text-light);
    display: flex; flex-direction: column; align-items: center;
    padding-top: 48px; font-size: 20px; line-height: 1.3; text-transform: uppercase;
  }
  .panel p { transform: scaleX(0.62); white-space: nowrap; }
  .panel .net { margin-top: 28px; font-size: 16px; }
  .cotton .brand-dot { background: var(--cotton-drop); }
  .cotton .scent-name { color: var(--cotton-name); }
  .cotton .band-rule { background: var(--cotton-rule); }
  .cotton .panel { background: linear-gradient(90deg, var(--cotton-panel-a), var(--cotton-panel-b)); }
  .lavender .brand-dot { background: var(--lavender-drop); }
  .lavender .scent-name { color: var(--lavender-name); }
  .lavender .panel { background: linear-gradient(90deg, var(--lavender-panel-a), var(--lavender-panel-b)); }
  .vine .brand-dot { background: var(--vine-drop); }
  .vine .scent-name { color: var(--vine-name); }
  .vine .panel { background: linear-gradient(90deg, var(--vine-panel-a), var(--vine-panel-b) 60%, #3b5a3a); }
  .fruity .brand-dot { background: var(--fruity-drop); }
  .fruity .scent-name { color: var(--fruity-name); }
  .fruity .panel { background: linear-gradient(90deg, var(--fruity-panel-a), var(--fruity-panel-b) 65%, #d99a36); color: var(--ink); }
</style>
</head>
<body>
  <main class="label-set">
    <article class="label cotton">
      <div class="brand"><span class="brand-dot"></span><span class="brand-name">Velmira</span></div>
      <h2 class="scent-name"><span>Cotton</span><span>Candy</span></h2>
      <div class="band-rule"></div>
      <section class="panel">
        <p>Non-Greesy &nbsp;•&nbsp; With Vitamin E</p>
        <p>Ultra Moisturizing</p>
        <p class="net">Net Wt. 4 Fl. Oz. (118 ml)</p>
      </section>
      <div class="type-box"><span>BODY OIL</span></div>
    </article>
    <article class="label lavender">
      <div class="brand"><span class="brand-dot"></span><span class="brand-name">Velmira</span></div>
      <h2 class="scent-name"><span>Soft</span><span>Lavender</span></h2>
      <div class="band-rule"></div>
      <section class="panel">
        <p>Non-Greesy &nbsp;•&nbsp; With Vitamin E</p>
        <p>Ultra Moisturizing</p>
        <p class="net">Net Wt. 4 Fl. Oz. (118 ml)</p>
      </section>
      <div class="type-box"><span>BODY OIL</span></div>
    </article>
    <article class="label vine">
      <div class="brand"><span class="brand-dot"></span><span class="brand-name">Velmira</span></div>
      <h2 class="scent-name"><span>Jungle</span><span>Vine</span></h2>
      <div class="band-rule"></div>
      <section class="panel">
        <p>Non-Greesy &nbsp;•&nbsp; With Vitamin E</p>
        <p>Ultra Moisturizing</p>
        <p class="net">Net Wt. 4 Fl. Oz. (118 ml)</p>
      </section>
      <div class="type-box"><span>BODY OIL</span></div>
    </article>
    <article class="label fruity">
      <div class="brand"><span class="brand-dot"></span><span class="brand-name">Velmira</span></div>
      <h2 class="scent-name"><span>Fruity</span><span>Delight</span></h2>
      <div class="band-rule"></div>
      <section class="panel">
        <p>Non-Greesy &nbsp;•&nbsp; With Vitamin E</p>
        <p>Ultra Moisturizing</p>
        <p class="net">Net Wt. 4 Fl. Oz. (118 ml)</p>
      </section>
      <div class="type-box"><span>BODY OIL</span></div>
    </article>
  </main>
</body>
</html>
```